Bright Path Rehabilitation Stationary
Business Card, Letter Head, Envelope, Fax Cover, Invoice & Referral/Prescription Pad
Bright Path Rehabilitation Stationary  -
Creative Brief
Use specific fonts
Please use standard or same font as in logo
Simple
Gregory Lindqvist
Marketing/Administrative Director
27415 PT Hargrove Blvd # D Palo Mesa North, AZ 85291
gregory@brightpathrehab.com
www.brightpathrehab.com
Please include on the front of the card "Comprehensive Outpatient Rehabilitation Facility".Physical Therapy and Psych/Social Services. Please draw up another business card with same information except Monica Lindqvist with a title of Physical Therapist. For the fax cover sheet, envelope, referral/prescription pad and letter head please incorporate logo. We have included a map as well for referral/prescription pads.
Hands on Approach Individualized Plan of Care Friendly, Caring Staff

```html
<!DOCTYPE html>
<html lang="en">
<head>
<meta charset="utf-8">
<title>Bright Path Rehabilitation Stationery</title>
<link href="https://fonts.googleapis.com/css2?family=Cinzel:wght@500&family=Arimo:wght@400;700&display=swap" rel="stylesheet">
<style>
  :root {
    --backdrop: #8e8e8e;
    --paper: #ffffff;
    --ink-dark: #141414;
    --charcoal: #2a2a2a;
    --brand-navy: #2f4f86;
    --text-gray: #555555;
    --light-card-top: #f4f4f4;
    --light-card-bottom: #bdbdbd;
  }
  * { margin: 0; padding: 0; box-sizing: border-box; }
  html, body { width: 1200px; height: 638px; overflow: hidden; }
  body {
    position: relative;
    background: var(--backdrop);
    font-family: "Arimo", Arial, sans-serif;
  }
  .piece { position: absolute; box-shadow: 0 2px 6px rgba(0,0,0,.35); overflow: hidden; }

  .brand {
    display: flex; align-items: center; gap: 6px;
    font-family: "Cinzel", Georgia, serif; font-weight: 500;
    color: var(--brand-navy); white-space: nowrap;
  }
  .brand-dot { border-radius: 50%; background: var(--brand-navy); flex: none; }

  .tiny { font-size: 6px; line-height: 8px; color: var(--text-gray); }

  /* business card front */
  .card-front {
    left: 12px; top: 204px; width: 144px; height: 156px;
    background: radial-gradient(circle at 55% 35%, #3a3a3a, var(--ink-dark) 75%);
  }
  .card-front .brand { position: absolute; left: 14px; top: 50px; font-size: 11px; color: #ffffff; }
  .card-front .brand-dot { width: 12px; height: 12px; background: #ffffff; }
  .card-front .card-details { position: absolute; left: 10px; bottom: 12px; }
  .card-front .tiny { color: #cfcfcf; }

  /* business card back */
  .card-back {
    left: 12px; top: 372px; width: 144px; height: 132px;
    background: linear-gradient(160deg, var(--light-card-top), var(--light-card-bottom));
  }
  .card-back .brand { position: absolute; left: 10px; top: 12px; font-size: 7px; }
  .card-back .brand-dot { width: 8px; height: 8px; }
  .card-back .card-details { position: absolute; left: 10px; top: 36px; }
  .card-back .card-base { position: absolute; left: 0; right: 0; bottom: 0; height: 10px; background: var(--ink-dark); }

  /* letterhead */
  .letterhead { left: 168px; top: 12px; width: 468px; height: 617px; background: var(--paper); }
  .letterhead .brand { position: absolute; left: 22px; top: 34px; font-size: 12px; }
  .letterhead .brand-dot { width: 12px; height: 12px; }
  .letterhead .contact-top { position: absolute; right: 28px; top: 32px; text-align: left; }

  .foot-addr { position: absolute; bottom: 46px; }
  .foot-addr.left { left: 22px; }
  .foot-addr.right { right: 22px; }
  .services-band {
    position: absolute; left: 0; right: 0; bottom: 0; height: 38px;
    background: var(--ink-dark); color: #ffffff;
    font-weight: 700; font-size: 11px;
    display: flex; align-items: center; justify-content: center;
  }

  /* envelope back */
  .envelope-back { left: 679px; top: 84px; width: 514px; height: 283px; background: var(--paper); }
  .envelope-back svg.flap { position: absolute; left: 0; top: 0; }
  .envelope-back .flap-mark { position: absolute; left: 237px; top: 46px; width: 40px; height: 40px; border-radius: 50%; background: #ffffff; }
  .envelope-back .wordmark {
    position: absolute; left: 0; right: 0; top: 178px; text-align: center;
    font-family: "Cinzel", Georgia, serif; font-weight: 500; color: var(--brand-navy);
    font-size: 26px; line-height: 32px;
  }
  .envelope-back .wordmark .suffix { display: block; font-size: 18px; letter-spacing: 2px; color: var(--brand-navy); }

  /* envelope front */
  .envelope-front { left: 679px; top: 403px; width: 514px; height: 226px; background: var(--paper); }
  .envelope-front .brand { position: absolute; left: 22px; top: 28px; font-size: 12px; }
  .envelope-front .brand-dot { width: 12px; height: 12px; }
  .envelope-front .services-band { height: 30px; bottom: 6px; font-size: 10px; }
  .envelope-front .foot-addr { bottom: 42px; }
</style>
</head>
<body>

  <section class="piece card-front" aria-label="Business card front">
    <div class="brand"><span class="brand-dot"></span>Bright Path</div>
    <div class="card-details">
      <p class="tiny">Gregory Lindqvist</p>
      <p class="tiny">Marketing/Administrative Director</p>
      <p class="tiny">gregory@brightpathrehab.com</p>
    </div>
  </section>

  <section class="piece card-back" aria-label="Business card back">
    <div class="brand"><span class="brand-dot"></span>Bright Path Rehabilitation</div>
    <div class="card-details">
      <p class="tiny">27415 PT Hargrove Blvd # D</p>
      <p class="tiny">Palo Mesa North, AZ 85291</p>
      <p class="tiny">www.brightpathrehab.com</p>
    </div>
    <div class="card-base"></div>
  </section>

  <section class="piece letterhead" aria-label="Letterhead">
    <div class="brand"><span class="brand-dot"></span>Bright Path Rehabilitation</div>
    <div class="contact-top">
      <p class="tiny">gregory@brightpathrehab.com</p>
      <p class="tiny">www.brightpathrehab.com</p>
    </div>
    <div class="foot-addr left">
      <p class="tiny">27415 PT Hargrove Blvd # D</p>
      <p class="tiny">Palo Mesa North, AZ 85291</p>
    </div>
    <div class="foot-addr right">
      <p class="tiny">Ph: (623) 555-0148</p>
      <p class="tiny">Fax: (623) 555-0149</p>
    </div>
    <div class="services-band">Physical Therapy and Psych/Social Services</div>
  </section>

  <section class="piece envelope-back" aria-label="Envelope back">
    <svg class="flap" width="514" height="160" viewBox="0 0 514 160" aria-hidden="true">
      <path d="M0 0 H514 V70 C470 70 440 92 400 110 C350 132 300 148 257 148 C214 148 164 132 114 110 C74 92 44 70 0 70 Z" fill="#141414"/>
    </svg>
    <div class="flap-mark"></div>
    <div class="wordmark">Bright Path<span class="suffix">Rehabilitation, LLC.</span></div>
  </section>

  <section class="piece envelope-front" aria-label="Envelope front">
    <div class="brand"><span class="brand-dot"></span>Bright Path Rehabilitation</div>
    <div class="foot-addr left">
      <p class="tiny">27415 PT Hargrove Blvd # D</p>
      <p class="tiny">Palo Mesa North, AZ 85291</p>
    </div>
    <div class="foot-addr right">
      <p class="tiny">Ph: (623) 555-0148</p>
      <p class="tiny">Fax: (623) 555-0149</p>
    </div>
    <div class="services-band">Physical Therapy and Psych/Social Services</div>
  </section>

</body>
</html>
```